Tova Meadows brand , chocolate packaging design

Tova Meadows

Products List

CANNABIS INFUSED CHOCOLATE BAR
(4 Flavor Chocolate Bar)
Original Milk chocolate Bar
Cookies N Cream Bar
Strawberry Cheesecake Bar
S’mores Bar

Information Front
-1000 MG THC Per package
-100mg THC per serving
-Made with Belgian Chocolate
-Made with Quality California Cannabis Extracts
-Net weight of bar 50grams
-California triangle warning symbol
-Flavor of chocolate bar

Information Back

-10 Servings per package
-100 mg serving size

-Directions
Wait 1-2 hours for full effect before consuming more.
-Very potent , Keep out of reach of children

-Store at 68-77° F
-Will melt in prolonged heat
-California government warning and ad41notice website

Ingredient list

Milk chocolate Bar
MILK CHOCOLATE (SUGAR, COCOA BUTTER , UNSWEETENED CHOCOLATE, SUNFLOWER LECITHIN, VANILLA) , CANNABIS EXTRACT.
ALLERGENS-CONTAINS MILK

Strawberry Cheesecake
WHITE CHOCOLATE (SUGAR, COCOA BUTTER, WHOLE MILK POWDER ,SOY LECITHIN, NATURAL VANILLA FLAVOR) STRAWBERRY POWDER , STRAWBERRY EXTRACT , NATURAL FLAVORS, CANNABIS EXTRACT.

Cookies n cream
WHITE CHOCOLATE (SUGAR, COCOA BUTTER, WHOLE MILK POWDER ,SOY LECITHIN, NATURAL VANILLA FLAVOR) 9
KRUNDELS (SUGAR, WHITE RICE FLOUR, TAPIOCA STARCH, PALM OIL, CANOLA OIL, WHOLE OAT FLOUR, CORN STARCH , COCOA (PROCESSED WITH ALKALI), INVERT SUGAR, SOY LECITHIN, BAKING SODA, SALT, XANTHAM GUM , CHOCOLATE, ARTIFICIAL FLAVOR, CANNABIS EXTRACT

S’mores
MILK CHOCOLATE (SUGAR, COCOA BUTTER, MILK, UNSWEETENED CHOCOLATE ,SUNFLOWER LECITHIN, VANILLA), MARSHMALLOW (SUGAR ,CORN SYRUP , MODIFIED STARCH, GELATIN, SODIUM HEXAMETAPHOSPHATE, ARTIFICIAL FLAVOR , NATURAL FLAVOR , ARTIFICIAL COLO (BLUE 1)), GRAHAM CRACKER (CORN STARCH, BROWN SUGAR , CORN FLOUR, PALM FAT , SOY FLOUR , SOY BRAN, HONEY, MODIFIED TAPIOCA STARCH, AMMONIUM BICARBONATE, BAKING SODA, SALT, CARAMELIZED SUGAR) NATURAL FLAVOR, CANNABIS EXTRACT.

Looking for simple clean modern design , chocolate bar can be like marivel of like the Brisbury one with images on it , and gummy is a mylar bag I really like the Brisbury style , I can provide dieline etc thank you !

Target Market(s)

Young adults

Industry/Entity Type

Cannabis , Delta 8 , CBD

Requirements
Must have
• Chocolate bar is box , dielines Included with images
Nice to have
• Simple clean , elegant and modern design , like the marivel and Brisbury brands , white logo preferred

```html
<!DOCTYPE html>
<html lang="en">
<head>
<meta charset="utf-8">
<title>Tova Meadows – Cannabis Infused Chocolate Bar Dielines</title>
<link rel="stylesheet" href="https://fonts.googleapis.com/css2?family=Questrial&family=Didact+Gothic&family=Archivo+Narrow:wght@400;700&family=Archivo+Black&display=swap">
<style>
:root{
  --paper:#ffffff;
  --ink:#000000;
  --white:#ffffff;
  --milk-deep:#070402;
  --milk-warm:#a0601a;
  --milk-accent:#f3b35a;
  --milk-name:#f6c77a;
  --cookie-deep:#22061e;
  --cookie-warm:#8a0f3c;
  --cookie-accent:#ffc928;
  --cookie-name:#ffd23a;
  --berry-deep:#24102c;
  --berry-warm:#c78ee6;
  --berry-accent:#ff2430;
  --berry-name:#ffffff;
  --sans:"Questrial", "Didact Gothic", sans-serif;
  --label:"Archivo Narrow", "Arial Narrow", sans-serif;
}
*{box-sizing:border-box;margin:0;padding:0}
html,body{width:1200px;height:657px;overflow:hidden;background:var(--paper)}
.canvas{position:relative;width:1200px;height:657px;background:var(--paper);font-family:var(--sans)}

.dieline{position:absolute;top:110px;width:372px;height:442px}
.dieline--milk{left:40px;--deep:var(--milk-deep);--warm:var(--milk-warm);--accent:var(--milk-accent);--name:var(--milk-name);--text-accent:var(--milk-accent)}
.dieline--cookie{left:424px;--deep:var(--cookie-deep);--warm:var(--cookie-warm);--accent:var(--cookie-accent);--name:var(--cookie-name);--text-accent:var(--cookie-accent)}
.dieline--berry{left:806px;--deep:var(--berry-deep);--warm:var(--berry-warm);--accent:var(--berry-accent);--name:var(--berry-name);--text-accent:var(--white)}

.piece{position:absolute}
.glue{left:0;top:50px;width:23px;height:343px;background:linear-gradient(90deg,var(--deep),var(--warm));clip-path:polygon(100% 0,0 8%,0 92%,100% 100%)}
.tuck{left:22px;width:152px;height:28px;background:linear-gradient(180deg,var(--warm),var(--deep))}
.tuck--top{top:0;border-radius:14px 14px 0 0;background:linear-gradient(180deg,var(--deep) 20%,var(--warm))}
.tuck--bottom{top:414px;border-radius:0 0 14px 14px}
.dust{left:18px;width:160px;height:24px;background:linear-gradient(180deg,var(--deep),var(--warm))}
.dust--top{top:22px}
.dust--bottom{top:392px;background:linear-gradient(180deg,var(--warm),var(--deep))}
.side{left:174px;top:20px;width:27px;height:402px;background:linear-gradient(90deg,var(--deep),var(--warm) 60%,var(--deep));clip-path:polygon(0 0,70% 0,100% 8%,100% 92%,70% 100%,0 100%)}
.rside{left:352px;top:20px;width:20px;height:402px;background:linear-gradient(90deg,var(--warm),var(--deep));clip-path:polygon(30% 0,100% 0,100% 100%,30% 100%,0 92%,0 8%)}

.front,.back{top:45px;width:152px;height:351px;overflow:hidden}
.front{left:22px;background:radial-gradient(ellipse 90% 55% at 50% 55%,var(--warm),var(--deep) 95%)}
.back{left:200px;background:radial-gradient(ellipse 95% 60% at 50% 50%,var(--warm),var(--deep) 100%)}
.dieline--berry .front,.dieline--berry .back{background:linear-gradient(90deg,var(--warm),var(--deep) 45%,var(--deep) 55%,var(--warm))}

.brand{position:absolute;top:30px;left:0;width:100%;text-align:center;font-family:var(--sans);font-size:16px;letter-spacing:1px;color:var(--white);line-height:18px;white-space:nowrap}
.product-type{position:absolute;top:52px;left:19px;width:114px;height:33px;background:var(--ink);color:var(--accent);font-size:9.2px;line-height:13px;text-align:center;padding-top:4px}
.product-shot{position:absolute;top:90px;left:10px;width:142px;height:112px;border-radius:6px}
.dieline--milk .product-shot{background:radial-gradient(ellipse at 60% 40%,#9a5a2a,#e8e0d8 55%,transparent 80%)}
.dieline--cookie .product-shot{background:radial-gradient(circle at 50% 50%,#d49a48,#6a2c12 60%,transparent 80%)}
.dieline--berry .product-shot{background:radial-gradient(ellipse at 55% 45%,#e8442a,#4a1030 65%,transparent 85%)}
.product-name{position:absolute;top:204px;left:0;width:100%;text-align:center;font-family:"Didact Gothic",sans-serif;font-size:18px;line-height:17px;color:var(--name)}
.dose{position:absolute;top:250px;left:12px;display:flex;gap:6px;align-items:center;color:var(--white);font-size:8.3px;line-height:10px;white-space:nowrap}
.dose svg{flex:none}
.claims{position:absolute;top:284px;left:0;width:100%;text-align:center;color:var(--white);font-size:8.4px;line-height:10px}
.rule{position:absolute;top:318px;left:42px;width:70px;height:1px;background:var(--white)}
.front-foot{position:absolute;top:326px;left:5px;right:5px;height:18px;display:flex;justify-content:space-between;align-items:flex-end;font-size:6.3px;color:var(--white);line-height:7.5px;white-space:nowrap}
.front-foot .flavor{color:var(--text-accent)}
.dieline--berry .front-foot .flavor{text-align:center}

.nutrition{position:absolute;top:10px;left:10px;width:133px;background:var(--white);padding:3px;font-family:var(--label);color:var(--ink)}
.nutrition-inner{border:1px solid var(--ink);padding:1px 3px}
.nf-title{font-family:"Archivo Black",sans-serif;font-size:13.2px;line-height:15px;letter-spacing:.3px;white-space:nowrap}
.nf-line{font-size:7px;line-height:9px;display:flex;justify-content:space-between;border-top:.5px solid #666}
.nf-line.plain{border:none}
.nf-line.indent{padding-left:6px}
.nf-line.indent2{padding-left:12px}
.nf-line b{font-weight:700}
.nf-bar{height:4px;background:var(--ink);margin:1px 0}
.nf-cal{display:flex;justify-content:space-between;align-items:flex-end;font-weight:700;font-size:12px;line-height:14px}
.nf-cal span:last-child{font-size:16px}
.nf-small{font-size:4.2px;line-height:5px;padding:1px 0}
.nf-dv{font-size:4.5px;text-align:right;line-height:6px}

.back-column{position:absolute;top:230px;left:10px;width:140px;height:102px;display:flex;flex-direction:column;gap:5px;overflow:hidden}
.back-copy{font-size:6px;line-height:7.2px;color:var(--text-accent)}
.back-copy .label{color:var(--white)}
.back-copy .caps{display:block;font-size:3.4px;line-height:4.2px;font-weight:700}
.dieline--berry .back-copy .caps{font-size:4.3px;line-height:5px}
.back-foot{position:absolute;top:337px;left:8px;right:8px;display:flex;justify-content:space-between;color:var(--white);font-size:6.4px;white-space:nowrap}
</style>
</head>
<body>
<main class="canvas">

  <!-- Original Milk Chocolate -->
  <section class="dieline dieline--milk">
    <div class="piece glue"></div>
    <div class="piece tuck tuck--top"></div>
    <div class="piece dust dust--top"></div>
    <div class="piece dust dust--bottom"></div>
    <div class="piece tuck tuck--bottom"></div>
    <div class="piece side"></div>
    <div class="piece rside"></div>
    <div class="piece front">
      <div class="brand">TOVA MEADOWS</div>
      <div class="product-type">CANNABIS INFUSED<br>CHOCOLATE BAR</div>
      <div class="product-shot" role="img" aria-label="Milk chocolate squares with a splash of milk"></div>
      <div class="product-name">Original Milk<br>Chocolate Bar</div>
      <div class="dose">
        <svg width="20" height="20" viewBox="0 0 20 20"><path d="M10 2 L18.5 17 H1.5 Z" fill="none" stroke="#fff" stroke-width="1.6"/></svg>
        <div>1000 MG THC Per package<br>100 mg THC per serving</div>
      </div>
      <div class="claims">Made with Belgian Chocolate<br>Made with Quality California<br>Cannabis Extracts</div>
      <div class="rule"></div>
      <div class="front-foot"><span class="flavor">Chocolate Flavor</span><span>Net weight 50 grams</span></div>
    </div>
    <div class="piece back">
      <div class="nutrition"><div class="nutrition-inner">
        <div class="nf-title">Nutrition Facts</div>
        <div class="nf-line plain">10 servings per container</div>
        <div class="nf-line plain"><b>Serving size</b><b>1 Square (5g)</b></div>
        <div class="nf-bar"></div>
        <div class="nf-small"><b>Amount Per Serving</b></div>
        <div class="nf-cal"><span>Calories</span><span>20</span></div>
        <div class="nf-bar"></div>
        <div class="nf-dv">% Daily Value*</div>
        <div class="nf-line"><span><b>Total Fat</b> 2g</span><span>3%</span></div>
        <div class="nf-line indent"><span>Saturated Fat 1g</span><span>5%</span></div>
        <div class="nf-line indent"><span><i>Trans</i> Fat 0g</span><span></span></div>
        <div class="nf-line"><span><b>Cholesterol</b> 0mg</span><span>0%</span></div>
        <div class="nf-line"><span><b>Sodium</b> 0mg</span><span>0%</span></div>
        <div class="nf-line"><span><b>Total Carbohydrate</b> 3g</span><span>1%</span></div>
        <div class="nf-line indent"><span>Dietary Fiber 0g</span><span>0%</span></div>
        <div class="nf-line indent"><span>Total Sugars 3g</span><span></span></div>
        <div class="nf-line indent2"><span>Includes 0g Added Sugars</span><span>0%</span></div>
        <div class="nf-line"><span><b>Protein</b> 0g</span><span>0%</span></div>
        <div class="nf-bar"></div>
        <div class="nf-small">Not a significant source of vitamin D, calcium, iron, and potassium</div>
        <div class="nf-small">* The % Daily Value (DV) tells you how much a nutrient in a serving of food contributes to a daily diet. 2,000 calories a day is used for general nutrition advice.</div>
      </div></div>
      <div class="back-column">
        <div class="back-copy"><span class="label">Ingredients list:</span><br>Milk Chocolate (Sugar, Cocoa Butter, Unsweetened Chocolate, Sunflower Cecithin, Vanilla), Cannabis Extract. Allergens - Contains Milk</div>
        <div class="back-copy"><span class="label">Directions:</span><br>Wait 1-2 hours for full effect before consuming more. Very potent, Keep out of reach of children</div>
        <div class="back-copy">Store at 68-77°F<br>California government warning and ad41notice website</div>
      </div>
      <div class="back-foot"><span>10 Servings per package</span><span>100 mg serving size</span></div>
    </div>
  </section>

  <!-- Cookies N Cream -->
  <section class="dieline dieline--cookie">
    <div class="piece glue"></div>
    <div class="piece tuck tuck--top"></div>
    <div class="piece dust dust--top"></div>
    <div class="piece dust dust--bottom"></div>
    <div class="piece tuck tuck--bottom"></div>
    <div class="piece side"></div>
    <div class="piece rside"></div>
    <div class="piece front">
      <div class="brand">TOVA MEADOWS</div>
      <div class="product-type">CANNABIS INFUSED<br>CHOCOLATE BAR</div>
      <div class="product-shot" role="img" aria-label="Chocolate chip cookie wrapped in a chocolate splash"></div>
      <div class="product-name">Cookies<br>N Cream Bar</div>
      <div class="dose">
        <svg width="20" height="20" viewBox="0 0 20 20"><path d="M10 2 L18.5 17 H1.5 Z" fill="none" stroke="#fff" stroke-width="1.6"/></svg>
        <div>1000 MG THC Per package<br>100 mg THC per serving</div>
      </div>
      <div class="claims">Made with Belgian Chocolate<br>Made with Quality California<br>Cannabis Extracts</div>
      <div class="rule"></div>
      <div class="front-foot"><span class="flavor">Cookies N Cream Flavor</span><span>Net weight 50 grams</span></div>
    </div>
    <div class="piece back">
      <div class="nutrition"><div class="nutrition-inner">
        <div class="nf-title">Nutrition Facts</div>
        <div class="nf-line plain">10 servings per container</div>
        <div class="nf-line plain"><b>Serving size</b><b>1 Square (5g)</b></div>
        <div class="nf-bar"></div>
        <div class="nf-small"><b>Amount Per Serving</b></div>
        <div class="nf-cal"><span>Calories</span><span>20</span></div>
        <div class="nf-bar"></div>
        <div class="nf-dv">% Daily Value*</div>
        <div class="nf-line"><span><b>Total Fat</b> 2g</span><span>3%</span></div>
        <div class="nf-line indent"><span>Saturated Fat 1g</span><span>5%</span></div>
        <div class="nf-line indent"><span><i>Trans</i> Fat 0g</span><span></span></div>
        <div class="nf-line"><span><b>Cholesterol</b> 0mg</span><span>0%</span></div>
        <div class="nf-line"><span><b>Sodium</b> 0mg</span><span>0%</span></div>
        <div class="nf-line"><span><b>Total Carbohydrate</b> 3g</span><span>1%</span></div>
        <div class="nf-line indent"><span>Dietary Fiber 0g</span><span>0%</span></div>
        <div class="nf-line indent"><span>Total Sugars 3g</span><span></span></div>
        <div class="nf-line indent2"><span>Includes 0g Added Sugars</span><span>0%</span></div>
        <div class="nf-line"><span><b>Protein</b> 0g</span><span>0%</span></div>
        <div class="nf-bar"></div>
        <div class="nf-small">Not a significant source of vitamin D, calcium, iron, and potassium</div>
        <div class="nf-small">* The % Daily Value (DV) tells you how much a nutrient in a serving of food contributes to a daily diet. 2,000 calories a day is used for general nutrition advice.</div>
      </div></div>
      <div class="back-column">
        <div class="back-copy"><span class="label">Ingredients list:</span>
          <span class="caps">WHITE CHOCOLATE (SUGAR, COCOA BUTTER, WHOLE MILK POWDER ,SOY LECITHIN, NATURAL VANILLA FLAVOR) 9</span>
          <span class="caps">KRUNDELS (SUGAR, WHITE RICE FLOUR, TAPIOCA STARCH, PALM OIL, CANOLA OIL, WHOLE OAT FLOUR, CORN STARCH , COCOA (PROCESSED WITH ALKALI), INVERT SUGAR, SOY LECITHIN, BAKING SODA, SALT, XANTHAM GUM , CHOCOLATE, ARTIFICIAL FLAVOR, CANNABIS EXTRACT</span></div>
        <div class="back-copy"><span class="label">Directions:</span><br>Wait 1-2 hours for full effect before consuming more. Very potent, Keep out of reach of children</div>
        <div class="back-copy">Store at 68-77°F<br>California government warning and ad41notice website</div>
      </div>
      <div class="back-foot"><span>10 Servings per package</span><span>100 mg serving size</span></div>
    </div>
  </section>

  <!-- Strawberry Cheesecake -->
  <section class="dieline dieline--berry">
    <div class="piece glue"></div>
    <div class="piece tuck tuck--top"></div>
    <div class="piece dust dust--top"></div>
    <div class="piece dust dust--bottom"></div>
    <div class="piece tuck tuck--bottom"></div>
    <div class="piece side"></div>
    <div class="piece rside"></div>
    <div class="piece front">
      <div class="brand">TOVA MEADOWS</div>
      <div class="product-type">CANNABIS INFUSED<br>CHOCOLATE BAR</div>
      <div class="product-shot" role="img" aria-label="Cut strawberries over a chocolate cheesecake cup"></div>
      <div class="product-name">Strawberry<br>Cheesecake Bar</div>
      <div class="dose">
        <svg width="20" height="20" viewBox="0 0 20 20"><path d="M10 2 L18.5 17 H1.5 Z" fill="none" stroke="#fff" stroke-width="1.6"/></svg>
        <div>1000 MG THC Per package<br>100 mg THC per serving</div>
      </div>
      <div class="claims">Made with Belgian Chocolate<br>Made with Quality California<br>Cannabis Extracts</div>
      <div class="rule"></div>
      <div class="front-foot"><span class="flavor">Strawberry<br>Cheesecake Flavor</span><span>Net weight 50 grams</span></div>
    </div>
    <div class="piece back">
      <div class="nutrition"><div class="nutrition-inner">
        <div class="nf-title">Nutrition Facts</div>
        <div class="nf-line plain">10 servings per container</div>
        <div class="nf-line plain"><b>Serving size</b><b>1 Square (5g)</b></div>
        <div class="nf-bar"></div>
        <div class="nf-small"><b>Amount Per Serving</b></div>
        <div class="nf-cal"><span>Calories</span><span>20</span></div>
        <div class="nf-bar"></div>
        <div class="nf-dv">% Daily Value*</div>
        <div class="nf-line"><span><b>Total Fat</b> 2g</span><span>3%</span></div>
        <div class="nf-line indent"><span>Saturated Fat 1g</span><span>5%</span></div>
        <div class="nf-line indent"><span><i>Trans</i> Fat 0g</span><span></span></div>
        <div class="nf-line"><span><b>Cholesterol</b> 0mg</span><span>0%</span></div>
        <div class="nf-line"><span><b>Sodium</b> 0mg</span><span>0%</span></div>
        <div class="nf-line"><span><b>Total Carbohydrate</b> 3g</span><span>1%</span></div>
        <div class="nf-line indent"><span>Dietary Fiber 0g</span><span>0%</span></div>
        <div class="nf-line indent"><span>Total Sugars 3g</span><span></span></div>
        <div class="nf-line indent2"><span>Includes 0g Added Sugars</span><span>0%</span></div>
        <div class="nf-line"><span><b>Protein</b> 0g</span><span>0%</span></div>
        <div class="nf-bar"></div>
        <div class="nf-small">Not a significant source of vitamin D, calcium, iron, and potassium</div>
        <div class="nf-small">* The % Daily Value (DV) tells you how much a nutrient in a serving of food contributes to a daily diet. 2,000 calories a day is used for general nutrition advice.</div>
      </div></div>
      <div class="back-column">
        <div class="back-copy"><span class="label">Ingredients list:</span>
          <span class="caps">WHITE CHOCOLATE (SUGAR, COCOA BUTTER, WHOLE MILK POWDER ,SOY LECITHIN, NATURAL VANILLA FLAVOR) STRAWBERRY POWDER , STRAWBERRY EXTRACT , NATURAL FLAVORS, CANNABIS EXTRACT.</span></div>
        <div class="back-copy"><span class="label">Directions:</span><br>Wait 1-2 hours for full effect before consuming more. Very potent, Keep out of reach of children</div>
        <div class="back-copy">Store at 68-77°F<br>California government warning and ad41notice website</div>
      </div>
      <div class="back-foot"><span>10 Servings per package</span><span>100 mg serving size</span></div>
    </div>
  </section>

</main>
</body>
</html>
```